NOLV.
ENCOMPASSING YOU
NOLV. -
Creative Brief
Use specific fonts
any thing which suits with the LOGO provided
Professional
RAHUL MEHTA
MR.
D-47, NORTH PARK-III, GURGAON 122019, HARYANA, INDIA
rahul@nolv.co
www.nolv.co
use logo at centre

```html
<!DOCTYPE html>
<html lang="en">
<head>
<meta charset="utf-8">
<title>NOLV. Business Card</title>
<link href="https://fonts.googleapis.com/css2?family=Roboto+Condensed:wght@400;700&display=swap" rel="stylesheet">
<style>
  :root {
    --page-bg: #e9e7e4;
    --card-bg: #ffffff;
    --brand-red: #d8232a;
    --ink: #1c1c1c;
    --text-grey: #555555;
    --rule-grey: #c8c8c8;
  }
  * { margin: 0; padding: 0; box-sizing: border-box; }
  html, body {
    width: 1200px; height: 852px; overflow: hidden;
    background: var(--page-bg);
    font-family: "Roboto Condensed", Arial, sans-serif;
  }
  .card {
    position: absolute; left: 100px; top: 140px;
    width: 1000px; height: 572px;
    background: var(--card-bg);
    border-radius: 34px;
    overflow: hidden;
    box-shadow: 0 10px 30px rgba(0,0,0,0.18);
  }
  .card__swoosh { position: absolute; inset: 0; }
  .brand {
    position: absolute; left: 250px; top: 90px;
    display: flex; align-items: center; gap: 26px;
  }
  .brand__mark {
    width: 110px; height: 110px; background: var(--brand-red);
  }
  .brand__name {
    font-weight: 700; font-size: 150px; line-height: 0.9;
    color: var(--brand-red); letter-spacing: 2px;
  }
  .holder {
    position: absolute; left: 250px; top: 390px;
    padding-right: 30px;
    border-right: 2px solid var(--rule-grey);
  }
  .holder__name {
    font-weight: 700; font-size: 40px; color: var(--brand-red);
    letter-spacing: 1px; margin-bottom: 12px;
  }
  .holder__address {
    font-size: 26px; line-height: 1.25; color: var(--text-grey);
  }
  .contacts {
    position: absolute; left: 640px; top: 300px;
    list-style: none;
  }
  .contacts__item {
    display: flex; align-items: center; gap: 16px;
    font-size: 27px; color: var(--text-grey);
    height: 44px;
  }
  .contacts__icon { width: 26px; height: 26px; flex: none; }
</style>
</head>
<body>
  <div class="card">
    <svg class="card__swoosh" width="1000" height="572" viewBox="0 0 1000 572">
      <defs>
        <linearGradient id="swooshRed" x1="0" y1="0" x2="1" y2="1">
          <stop offset="0" stop-color="#e8353b"/>
          <stop offset="1" stop-color="#a5151b"/>
        </linearGradient>
      </defs>
      <path d="M0,120 C40,280 80,430 150,572 L0,572 Z" fill="url(#swooshRed)"/>
      <path d="M0,40 C70,230 130,420 200,572" fill="none" stroke="#1c1c1c" stroke-width="7"/>
    </svg>

    <div class="brand">
      <div class="brand__mark"></div>
      <div class="brand__name">NOLV.</div>
    </div>

    <div class="holder">
      <div class="holder__name">RAHUL MEHTA</div>
      <div class="holder__address">D-47, North Park-III,<br>Gurgaon 122019,<br>Haryana, India</div>
    </div>

    <ul class="contacts">
      <li class="contacts__item">
        <svg class="contacts__icon" viewBox="0 0 24 24"><path d="M6 2 L10 2 L11 7 L8 9 C9 12 12 15 15 16 L17 13 L22 14 L22 18 C22 20 20 22 18 22 C9 21 3 15 2 6 C2 4 4 2 6 2 Z" fill="#d8232a"/></svg>
        +91-124-5550182
      </li>
      <li class="contacts__item">
        <svg class="contacts__icon" viewBox="0 0 24 24"><rect x="6" y="1" width="12" height="22" rx="2" fill="#d8232a"/><rect x="8" y="4" width="8" height="13" fill="#fff"/><circle cx="12" cy="20" r="1.3" fill="#fff"/></svg>
        +91-9000400217
      </li>
      <li class="contacts__item">
        <svg class="contacts__icon" viewBox="0 0 24 24"><rect x="6" y="2" width="12" height="6" fill="#d8232a"/><rect x="2" y="9" width="20" height="9" rx="2" fill="#d8232a"/><rect x="6" y="15" width="12" height="7" fill="#fff" stroke="#d8232a" stroke-width="2"/></svg>
        +91-124-5550193
      </li>
      <li class="contacts__item">
        <svg class="contacts__icon" viewBox="0 0 24 24"><circle cx="12" cy="12" r="4" fill="none" stroke="#d8232a" stroke-width="2.5"/><path d="M16 8 L16 14 C16 17 21 17 21 12 A9 9 0 1 0 16 20" fill="none" stroke="#d8232a" stroke-width="2.5"/></svg>
        rahul@nolv.co
      </li>
      <li class="contacts__item">
        <svg class="contacts__icon" viewBox="0 0 24 24"><circle cx="12" cy="12" r="10" fill="none" stroke="#d8232a" stroke-width="2"/><ellipse cx="12" cy="12" rx="4.5" ry="10" fill="none" stroke="#d8232a" stroke-width="2"/><path d="M2 12 H22" stroke="#d8232a" stroke-width="2"/></svg>
        www.nolv.co
      </li>
    </ul>
  </div>
</body>
</html>
```